quorvel stationary business card and letterhead

THIS PROJECT IS TO DESIGN A BUSINESS CARD DOUBLE SIDES .

Reason: I AM WAITING FOR BEZITH SUBMISION

Industry/Entity Type

Business

Font styles to use
Other font styles liked:
• Chose your font

```html
<!DOCTYPE html>
<html lang="en">
<head>
<meta charset="utf-8">
<title>Quorvel Stationery</title>
<link href="https://fonts.googleapis.com/css2?family=Cinzel:wght@600&family=Open+Sans:ital,wght@0,400;1,400&display=swap" rel="stylesheet">
<style>
  :root {
    --backdrop: #dcdcdc;
    --paper: #ffffff;
    --brand-yellow: #f8c70c;
    --brand-dark: #231f20;
    --light-text: #ffffff;
  }
  * { margin: 0; padding: 0; box-sizing: border-box; }
  html, body { width: 1200px; height: 900px; overflow: hidden; }
  body {
    position: relative;
    background: var(--backdrop);
    font-family: "Open Sans", Arial, sans-serif;
  }
  .letterhead {
    position: absolute;
    left: 118px; top: 13px;
    width: 620px; height: 876px;
    background: var(--paper);
    overflow: hidden;
  }
  .brand {
    position: absolute;
    display: flex;
    align-items: center;
    gap: 6px;
  }
  .brand-dot {
    border-radius: 50%;
    background: var(--brand-yellow);
    flex: none;
  }
  .brand-name {
    font-family: "Cinzel", Georgia, serif;
    font-weight: 600;
    line-height: 1;
    letter-spacing: 0.5px;
  }
  .letterhead-brand { right: 38px; top: 38px; }
  .letterhead-brand .brand-dot { width: 50px; height: 50px; }
  .letterhead-brand .brand-name { font-size: 34px; color: var(--brand-dark); }

  .letterhead-footer {
    position: absolute;
    left: 40px; top: 795px;
    width: 580px; height: 71px;
  }
  .footer-brand { left: 75px; top: 20px; }
  .footer-brand .brand-dot { width: 37px; height: 37px; }
  .footer-brand .brand-name { font-size: 14px; color: var(--light-text); }

  .contact {
    position: absolute;
    font-size: 7px;
    line-height: 10px;
    color: var(--light-text);
  }
  .letterhead-contact { right: 38px; top: 816px; text-align: right; }

  .card-shape { position: absolute; left: 0; top: 0; }

  .card-brand .brand-dot { width: 36px; height: 36px; }
  .card-brand .brand-name { font-size: 27px; }
  .card-front-brand { left: 846px; top: 327px; }
  .card-front-brand .brand-name { color: var(--light-text); }
  .card-back-brand { left: 851px; top: 491px; }
  .card-back-brand .brand-dot { background: var(--light-text); }
  .card-back-brand .brand-name { color: var(--brand-dark); }

  .card-person {
    position: absolute;
    right: 191px; top: 385px;
    text-align: right;
    color: var(--light-text);
  }
  .person-name { font-size: 9px; line-height: 12px; }
  .person-role { font-size: 7px; font-style: italic; line-height: 9px; }
  .card-contact { left: 891px; top: 550px; }
</style>
</head>
<body>
  <section class="letterhead">
    <div class="brand letterhead-brand">
      <span class="brand-dot"></span>
      <span class="brand-name">Quorvel</span>
    </div>

    <svg class="letterhead-footer" viewBox="0 0 580 71" aria-hidden="true">
      <path d="M 35 0 H 580 V 71 H 35 C 10 71 0 55 0 35 C 0 15 10 0 35 0 Z" fill="var(--brand-yellow)"/>
      <path d="M 55 5 H 580 V 71 H 55 C 30 71 20 55 20 38 C 20 20 30 5 55 5 Z" fill="var(--brand-dark)"/>
    </svg>
    <div class="brand footer-brand">
      <span class="brand-dot"></span>
      <span class="brand-name">Quorvel</span>
    </div>
    <p class="contact letterhead-contact">
      Lorem ipsum ave. 1234 B / London<br>
      Tel: 1234567890 Fax: 1234567890<br>
      www.quorvelconsulting.com
    </p>
  </section>

  <svg class="card-shape" width="1200" height="900" aria-hidden="true">
    <path class="card-front" d="M 850 289 H 1059 Q 1071 289 1071 301 V 429 Q 1071 441 1059 441 H 850 C 810 441 793 410 793 365 C 793 320 810 289 850 289 Z" fill="var(--brand-dark)"/>
    <path class="card-back" d="M 805 453 H 1014 C 1054 453 1071 484 1071 529 C 1071 574 1054 605 1014 605 H 805 Q 793 605 793 593 V 465 Q 793 453 805 453 Z" fill="var(--brand-yellow)"/>
  </svg>

  <div class="brand card-brand card-front-brand">
    <span class="brand-dot"></span>
    <span class="brand-name">Quorvel</span>
  </div>
  <div class="card-person">
    <p class="person-name">Name Surname</p>
    <p class="person-role">Financial affairs</p>
  </div>

  <div class="brand card-brand card-back-brand">
    <span class="brand-dot"></span>
    <span class="brand-name">Quorvel</span>
  </div>
  <p class="contact card-contact">
    Lorem ipsum ave. 1234 B / London<br>
    Tel: 1234567890 Fax: 1234567890<br>
    www.quorvelconsulting.com
  </p>
</body>
</html>
```